New Web Design Project- Willowbrook Elders

Willowbrook Elders is the Capital regions premiere, non-medical, in-home care & companionship service that unites "junior-senior" caregivers with "senior-senior" care recipients so that senior-seniors can remain safe & independent in their own homes.
Our compassionate "junior-senior" caregivers are all retirees that have already enjoyed rewarding careers and/or have raised families of their own and feel the need to pay-it-forward with their care for older seniors.
Services include grocery shopping, medical or dental appointments, errands, meal preparation & cleanup, light housekeeping, bed making, laundry, hobbies, reading, transportation, entertainment, games, mobility assistance/transfers, respite care, light yard work, pet walking.

Target Market(s)

Grown children of senior-seniors between who are between 55-70, predominantly the daughters (female). End users of services (senior-seniors) are typically 80-100 years old and living in own homes

Industry/Entity Type

Medical

Coding

Coded - Design and coding required

Number of Pages Required

5+ page

Font styles to use
Sans Serif

Colors
3277b5
ec1f27

Requirements
Must have
• supporting photos on each page. Contact us page. Promotional video (done) attached that doesn't take viewers off my site (https://vidhost.example/q7Rk2mPzL4n).
• Also, need my downloadable brochure (attached).
• The following pages:
• Home. Services. About Us. News. Employment. Contact us. Junior-Seniors Assisting Senior-Seniors. Why non-medical in-home care. Who are junior-seniors?Financial effects of senior care. Do you need care? Does someone you love need care?
Should not have
• Any other photos or images other than what I've supplied.

```html
<!DOCTYPE html>
<html lang="en">
<head>
<meta charset="utf-8">
<title>Willowbrook Elders</title>
<link href="https://fonts.googleapis.com/css2?family=Lato:wght@400;700;900&display=swap" rel="stylesheet">
<style>
:root{
  --blue:#1d4f9c;
  --blue-dark:#163e7d;
  --red:#e61e2a;
  --ink:#222;
  --grey:#555;
  --footer:#2b2b2b;
  --footer-text:#9a9a9a;
}
*{box-sizing:border-box;margin:0;padding:0}
html,body{width:1200px;height:2980px;overflow:hidden}
body{font-family:'Lato',sans-serif;color:var(--ink);background:#fff;position:relative}
.abs{position:absolute}
a{color:inherit;text-decoration:none}

/* header */
.site-header{position:absolute;left:0;top:0;width:1200px;height:138px;background:#fff}
.brand{position:absolute;left:90px;top:48px;display:flex;align-items:center;gap:12px}
.brand-mark{width:42px;height:42px;background:var(--blue)}
.brand-name{font-size:30px;font-weight:700;color:var(--blue-dark)}
.phone{position:absolute;right:90px;top:32px;font-size:18px;display:flex;align-items:center;gap:6px}
.main-nav{position:absolute;right:88px;top:78px;display:flex;gap:26px;font-size:18px;font-weight:700;color:#222}
.main-nav .active{color:var(--red)}

/* hero */
.hero{position:absolute;left:0;top:138px;width:1200px;height:580px;background:linear-gradient(110deg,#8d6b55 0%,#c9b59a 35%,#d9c6b0 55%,#6a6f78 100%);overflow:hidden}
.hero-card{position:absolute;left:80px;top:160px;width:495px;height:240px;background:rgba(29,79,156,.88);border-bottom:8px solid var(--red);border-radius:26px 0 0 0;color:#fff;padding:38px 52px}
.hero-card h1{font-weight:400;font-size:34px;line-height:1.1}
.hero-card h1 strong{display:block;font-size:42px;font-weight:700}
.hero-card p{font-size:17px;line-height:1.5;margin-top:10px}
.dots{position:absolute;left:552px;top:484px;display:flex;gap:10px}
.dots span{width:14px;height:14px;border-radius:50%;background:#333;border:2px solid #fff}
.dots span:first-child{background:transparent;border-color:#333}

/* intro */
.video{position:absolute;left:98px;top:768px;width:467px;height:298px;background:linear-gradient(120deg,#4a4a40,#8b7a60 50%,#6b6e70)}
.play{position:absolute;left:193px;top:109px;width:80px;height:80px;border-radius:50%;background:#fff}
.intro{position:absolute;left:604px;top:772px;width:530px}
.intro h2{font-size:40px;font-weight:400;color:#111}
.intro p{font-size:16.5px;line-height:31px;color:var(--grey);margin-top:22px}
.btn{display:inline-flex;align-items:center;justify-content:center;font-size:17px;font-weight:700}
.btn-outline-red{position:absolute;left:604px;top:998px;width:208px;height:44px;border:2px solid var(--red);color:var(--red)}
.btn-outline-blue{position:absolute;left:824px;top:998px;width:208px;height:44px;border:2px solid var(--blue);color:var(--blue)}

/* services */
.services{position:absolute;left:0;top:1158px;width:1200px;height:457px;background:linear-gradient(90deg,#1b4a95,#1f4f9c 50%,#234d8e);color:#fff}
.services h2{position:absolute;left:0;width:1200px;top:36px;text-align:center;font-size:32px;font-weight:400}
.service{position:absolute;top:116px;width:200px;text-align:center}
.service h3{font-size:17px;font-weight:700;margin-top:12px}
.service p{font-size:12.5px;line-height:19px;margin-top:6px;padding:0 12px;color:#dfe6f3}
.btn-outline-white{position:absolute;left:495px;top:372px;width:220px;height:48px;border:2px solid #fff;color:#fff;font-weight:400}

/* split */
.split-left{position:absolute;left:0;top:1615px;width:605px;height:430px;background:linear-gradient(120deg,#cfcfcf,#e9e9e9 50%,#c8c8c8)}
.split-right{position:absolute;left:605px;top:1615px;width:595px;height:430px;background:linear-gradient(120deg,#e8252c,#f0383d)}
.split-inner{position:absolute;top:112px;width:100%;text-align:center;padding:0 90px}
.split-inner h2{font-size:29px;line-height:32px;font-weight:700}
.split-inner p{font-size:14.5px;line-height:22px;margin-top:22px}
.btn-red{width:180px;height:44px;background:var(--red);color:#fff;font-weight:400;margin-top:32px}
.btn-blue{width:180px;height:44px;background:var(--blue-dark);color:#fff;font-weight:400;margin-top:32px}

/* news */
.news-title{position:absolute;left:92px;top:2098px;font-size:36px;font-weight:400}
.card{position:absolute;top:2172px;width:324px;height:368px;border:1px solid #ccc;background:#fff}
.card-img{height:204px;background:linear-gradient(120deg,#5e6b7a,#b8a98f 60%,#7c8a70)}
.date{position:absolute;left:12px;top:224px;width:60px;height:60px;border-radius:50%;background:var(--blue);color:#fff;text-align:center;font-size:25px;line-height:24px;padding-top:9px}
.date small{display:block;font-size:14px;line-height:14px}
.card-body{position:absolute;left:84px;top:224px;right:12px}
.card-body h3{font-size:17px;font-weight:400}
.card-body p{font-size:12.5px;line-height:19px;color:#666;margin-top:6px}
.card-body a{display:block;font-size:14px;font-weight:700;color:var(--blue);margin-top:8px}

/* footer */
.site-footer{position:absolute;left:0;top:2608px;width:1200px;height:372px;background:var(--footer);color:var(--footer-text)}
.f-col{position:absolute;top:54px}
.f-col h4{color:#fff;font-size:18px;font-weight:700;padding-bottom:6px;border-bottom:2px solid var(--red);display:inline-block}
.f-col ul{list-style:none;margin-top:16px}
.f-col li{font-size:15px;line-height:31px}
.contact li{display:flex;gap:10px;align-items:flex-start;line-height:26px;margin-bottom:4px}
.socials{display:flex;gap:8px;margin-top:10px}
.socials span{width:38px;height:38px;border-radius:50%;border:2px solid #ddd}
.f-rule{position:absolute;left:82px;top:308px;width:1036px;height:1px;background:#555}
.copyright{position:absolute;left:0;width:1200px;top:328px;text-align:center;font-size:13px}
</style>
</head>
<body>

<header class="site-header">
  <a class="brand" href="#"><span class="brand-mark"></span><span class="brand-name">Willowbrook Elders</span></a>
  <div class="phone">
    <svg width="18" height="18" viewBox="0 0 24 24"><path fill="#1d4f9c" d="M6.6 10.8a15 15 0 0 0 6.6 6.6l2.2-2.2c.3-.3.7-.4 1-.2 1.1.4 2.3.6 3.6.6.6 0 1 .4 1 1V20c0 .6-.4 1-1 1A17 17 0 0 1 3 4c0-.6.4-1 1-1h3.5c.6 0 1 .4 1 1 0 1.3.2 2.5.6 3.6.1.3 0 .7-.2 1z"/></svg>
    (555) 014-2290
  </div>
  <nav class="main-nav">
    <a class="active" href="#">Home</a><a href="#">Services</a><a href="#">About Us</a><a href="#">News</a><a href="#">Employment</a><a href="#">Contact us</a>
  </nav>
</header>

<section class="hero" role="img" aria-label="Photo: caregiver handing a basket of groceries to a smiling senior woman at her door">
  <div class="hero-card">
    <h1>Welcome to <strong>Willowbrook Elders</strong></h1>
    <p>Vivamus porttitor purus nisi eleifend libero a tempus libero lectus feugiat felis vlacus Ut ac mi quis</p>
  </div>
  <div class="dots"><span></span><span></span><span></span><span></span></div>
  <svg class="abs" style="left:0;top:500px" width="1200" height="80" viewBox="0 0 1200 80" preserveAspectRatio="none">
    <path d="M0 50 C300 14 700 40 1200 0 L1200 80 L0 80Z" fill="#1d4f9c"/>
    <path d="M0 58 C300 24 700 48 1200 10 L1200 80 L0 80Z" fill="#e61e2a"/>
    <path d="M0 78 C300 44 700 68 1200 30 L1200 80 L0 80Z" fill="#fff"/>
  </svg>
</section>

<section>
  <div class="video" role="img" aria-label="Promotional video still: two senior women standing outside a house">
    <div class="play"><svg width="80" height="80" viewBox="0 0 80 80"><path d="M32 24 L58 40 L32 56Z" fill="#222"/></svg></div>
  </div>
  <div class="intro">
    <h2>Willowbrook Elders</h2>
    <p>It can be hard to admit that aging makes certain things more difficult. Asking for help doesn’t mean giving up independence – it means preserving it. Receiving assistance from someone who understands how your loved one wants to live is the first step.</p>
  </div>
  <a class="btn btn-outline-red" href="#">Download Brochure</a>
  <a class="btn btn-outline-blue" href="#">Learn More</a>
</section>

<section class="services">
  <h2>Our Services</h2>
  <div class="service" style="left:60px">
    <svg width="120" height="130" viewBox="0 0 120 130"><path d="M60 2a58 58 0 0 1 10 115l-10 12-10-12A58 58 0 0 1 60 2z" fill="#fff"/><circle cx="60" cy="60" r="50" fill="#e61e2a"/><path d="M38 50h44l-6 26H44z M48 50l8-14 M72 50l-8-14" fill="none" stroke="#fff" stroke-width="4"/><path d="M50 56v16M60 56v16M70 56v16" stroke="#fff" stroke-width="3"/></svg>
    <h3>GROCERY SHOPPING</h3><p>Morbi diam mauris viverra in gravida eu mattis in ante Morbi eget arcu Morbi porta</p>
  </div>
  <div class="service" style="left:280px">
    <svg width="120" height="130" viewBox="0 0 120 130"><path d="M60 2a58 58 0 0 1 10 115l-10 12-10-12A58 58 0 0 1 60 2z" fill="#fff"/><circle cx="60" cy="60" r="50" fill="#e61e2a"/><circle cx="56" cy="36" r="5" fill="#fff"/><path d="M56 44v18h16l6 14" fill="none" stroke="#fff" stroke-width="4"/><path d="M48 52a14 14 0 1 0 18 20" fill="none" stroke="#fff" stroke-width="4"/></svg>
    <h3>MEDICAL</h3><p>Morbi diam mauris viverra in gravida eu mattis in ante Morbi eget arcu Morbi porta</p>
  </div>
  <div class="service" style="left:500px">
    <svg width="120" height="130" viewBox="0 0 120 130"><path d="M60 2a58 58 0 0 1 10 115l-10 12-10-12A58 58 0 0 1 60 2z" fill="#fff"/><circle cx="60" cy="60" r="50" fill="#e61e2a"/><path d="M34 56h52a26 22 0 0 1-52 0z" fill="#fff"/><path d="M50 46c-4-4 4-8 0-12M60 46c-4-4 4-8 0-12M70 46c-4-4 4-8 0-12" fill="none" stroke="#fff" stroke-width="3"/></svg>
    <h3>MEAL PREPARATION</h3><p>Morbi diam mauris viverra in gravida eu mattis in ante Morbi eget arcu Morbi porta</p>
  </div>
  <div class="service" style="left:715px">
    <svg width="120" height="130" viewBox="0 0 120 130"><path d="M60 2a58 58 0 0 1 10 115l-10 12-10-12A58 58 0 0 1 60 2z" fill="#fff"/><circle cx="60" cy="60" r="50" fill="#e61e2a"/><path d="M40 56l6-16h28l6 16v18H40z" fill="none" stroke="#fff" stroke-width="4"/><path d="M40 62h40" stroke="#fff" stroke-width="4"/></svg>
    <h3>BED MAKING</h3><p>Morbi diam mauris viverra in gravida eu mattis in ante Morbi eget arcu Morbi porta</p>
  </div>
  <div class="service" style="left:940px">
    <svg width="120" height="130" viewBox="0 0 120 130"><path d="M60 2a58 58 0 0 1 10 115l-10 12-10-12A58 58 0 0 1 60 2z" fill="#fff"/><circle cx="60" cy="60" r="50" fill="#e61e2a"/><rect x="40" y="34" width="40" height="50" rx="3" fill="none" stroke="#fff" stroke-width="4"/><path d="M40 44h40" stroke="#fff" stroke-width="3"/><circle cx="60" cy="64" r="11" fill="#fff"/></svg>
    <h3>LAUNDRY</h3><p>Morbi diam mauris viverra in gravida eu mattis in ante Morbi eget arcu Morbi porta</p>
  </div>
  <a class="btn btn-outline-white" href="#">View More Services</a>
</section>

<section class="split-left" role="img" aria-label="Photo: senior couple reviewing finances with a caregiver">
  <div class="split-inner" style="color:#111">
    <h2>The Financial Effects of<br>Senior Care</h2>
    <p style="color:#333">Our considerate and compassionate Active Retirees are professionally trained and skilled to provide you with the care you need to stay independent, comfortable, and safe in your home.</p>
    <a class="btn btn-red" href="#">Learn More</a>
  </div>
</section>
<section class="split-right" role="img" aria-label="Photo: retired caregiver with a senior woman, red tinted">
  <div class="split-inner" style="color:#fff">
    <h2>Active Retirees Caring<br>for Older Elders</h2>
    <p>Willowbrook Elders offers financial efficiency with in-home services provided at one quarter the cost of semi-private nursing homes and one third the cost of assisted living facilities.</p>
    <a class="btn btn-blue" href="#">Learn More</a>
  </div>
</section>

<section>
  <h2 class="news-title">Latest News</h2>
  <article class="card" style="left:90px">
    <div class="card-img" role="img" aria-label="Photo: caregiver serving tea to a senior woman"></div>
    <div class="date">15<small>AUG</small></div>
    <div class="card-body"><h3>Your Blog Tittle here</h3><p>netus et malesuada fames ac turpis egestas Cras id elit Integer quis urna Ut ante enim dapibus males</p><a href="#">READ MORE</a></div>
  </article>
  <article class="card" style="left:446px">
    <div class="card-img" role="img" aria-label="Photo: two senior women reading together on a sofa"></div>
    <div class="date">05<small>AUG</small></div>
    <div class="card-body"><h3>Your Blog Tittle here</h3><p>netus et malesuada fames ac turpis egestas Cras id elit Integer quis urna Ut ante enim dapibus males</p><a href="#">READ MORE</a></div>
  </article>
  <article class="card" style="left:794px">
    <div class="card-img" role="img" aria-label="Photo: senior woman laughing with a caregiver outdoors"></div>
    <div class="date">02<small>AUG</small></div>
    <div class="card-body"><h3>Your Blog Tittle here</h3><p>netus et malesuada fames ac turpis egestas Cras id elit Integer quis urna Ut ante enim dapibus males</p><a href="#">READ MORE</a></div>
  </article>
</section>

<footer class="site-footer">
  <div class="f-col" style="left:122px"><h4>OUR CENTRE</h4><ul><li>Home</li><li>About Us</li><li>Why Us</li><li>News</li></ul></div>
  <div class="f-col" style="left:336px"><h4>SERVICES</h4><ul><li>Grocery Shopping</li><li>Medical or dental</li><li>Meal Preparation &amp; cleanup</li><li>Light housekeeping</li></ul></div>
  <div class="f-col" style="left:620px;top:84px"><ul><li>Bed making</li><li>Laundry</li><li>Hobbies</li><li>Reading</li></ul></div>
  <div class="f-col contact" style="left:820px"><h4>CONTACT US</h4>
    <ul>
      <li><svg width="14" height="18" viewBox="0 0 14 18" style="margin-top:4px"><path d="M7 0a7 7 0 0 1 7 7c0 5-7 11-7 11S0 12 0 7a7 7 0 0 1 7-7z" fill="#ddd"/><circle cx="7" cy="7" r="2.5" fill="#2b2b2b"/></svg><span>P.O. Box 418, Maple Hollow,<br>New York 10990</span></li>
      <li><svg width="14" height="14" viewBox="0 0 24 24" style="margin-top:6px"><path fill="#ddd" d="M6.6 10.8a15 15 0 0 0 6.6 6.6l2.2-2.2c.3-.3.7-.4 1-.2 1.1.4 2.3.6 3.6.6.6 0 1 .4 1 1V20c0 .6-.4 1-1 1A17 17 0 0 1 3 4c0-.6.4-1 1-1h3.5c.6 0 1 .4 1 1 0 1.3.2 2.5.6 3.6.1.3 0 .7-.2 1z"/></svg><span>(555) 014-2290</span></li>
      <li><svg width="14" height="12" viewBox="0 0 14 12" style="margin-top:7px"><rect width="14" height="12" fill="#ddd"/><path d="M0 0l7 6 7-6" fill="none" stroke="#2b2b2b" stroke-width="1.5"/></svg><span>Email Us</span></li>
    </ul>
    <div class="socials"><span></span><span></span><span></span><span></span></div>
  </div>
  <div class="f-rule"></div>
  <p class="copyright">© 2017 Company Name. All right reserved</p>
</footer>

</body>
</html>
```